App Design Project

Hello,
I'm looking for a great designer for my iOS Applications, we have a lot of works and we're short in designers :(
I want to revamp my thermometer iOS app. You will find attached the images I want to replace. I need something with the same element (temp, condition, weather icon) but with a different look!
Same, new icon, you have carte blanche to this one.
I want a design that stands out from the hundreds of weather application that almost all the same design. I am looking for something that does say "wow, it rocks."
Please do not Provide classic design that we can see everywhere ... I'm looking for something with a real artistic choice, contrast, colours, etc.
As a marketing screenshot, I want something classic, you'll find an example attached, feel free to innovate.
To sum-up :
- One new view for my App
- One new icon
- One marketing screenshot

```html
<!DOCTYPE html>
<html lang="en">
<head>
<meta charset="utf-8">
<title>Thermometer for Orbphone – marketing screens</title>
<link href="https://fonts.googleapis.com/css2?family=Oswald:wght@400;600&family=Advent+Pro:wght@200;400;600&family=Exo+2:wght@500&display=swap" rel="stylesheet">
<style>
  :root{
    --slate-top:#5b5c5e;
    --slate-bottom:#3d3e40;
    --divider:#7a8786;
    --sky-blue:#29a6e9;
    --white:#ffffff;
    --ink:#1d1f22;
    --strip:#2a2c2f;
    --tag:#3a3b3d;
    --snow-light:#c9d3dc;
    --snow-mid:#8f9ead;
    --snow-dark:#4d5763;
    --rain-light:#9aa59b;
    --rain-mid:#56615a;
    --rain-dark:#1c2220;
    --ring-track:#16181a;
  }
  *{box-sizing:border-box;margin:0;padding:0}
  html,body{width:1200px;height:1000px;overflow:hidden;background:var(--divider)}
  .canvas{position:relative;width:1200px;height:1000px;background:linear-gradient(90deg,#6c7878,var(--divider) 50%,#6c7878)}
  .panel{position:absolute;top:0;width:568px;height:1000px;overflow:hidden;
    background:linear-gradient(180deg,var(--slate-top),var(--slate-bottom))}
  .panel.left{left:0}
  .panel.right{left:632px}

  .headline{position:absolute;left:0;width:568px;top:62px;text-align:center;padding-left:250px;color:var(--white);font-family:"Oswald",sans-serif}
  .headline .app-name{display:block;font-weight:600;font-size:33px;letter-spacing:.5px;line-height:40px}
  .headline .platform{display:block;font-weight:400;font-size:27px;line-height:34px}

  .callouts{position:absolute;left:0;top:0;width:568px;height:560px}
  .callouts text{font-family:"Exo 2",sans-serif;font-size:19px;fill:var(--white);letter-spacing:1px}
  .callouts .reading{font-family:"Advent Pro",sans-serif;font-weight:600;font-size:26px;letter-spacing:1px}

  /* app screen */
  .screen{position:absolute;width:232px;height:392px;background:var(--ink);overflow:hidden;font-family:"Advent Pro",sans-serif;color:var(--white)}
  .scene{position:absolute;left:0;top:0;width:232px;height:292px}
  .snow .scene{background:linear-gradient(170deg,var(--snow-light) 0%,#aab7c3 35%,var(--snow-mid) 65%,var(--snow-dark) 100%)}
  .rain .scene{background:linear-gradient(165deg,var(--rain-light) 0%,var(--rain-mid) 45%,var(--rain-dark) 100%)}
  .location{position:absolute;right:6px;top:8px;background:var(--tag);font-size:9px;font-weight:600;letter-spacing:.5px;padding:2px 8px}
  .condition-icon{position:absolute;left:62px;top:70px;width:108px;height:86px}
  .condition{position:absolute;left:0;width:232px;top:160px;text-align:center;font-weight:200;font-size:34px;letter-spacing:2px}
  .rule{position:absolute;left:0;width:232px;height:1px;background:rgba(255,255,255,.45)}
  .rule.upper{top:205px}
  .rule.lower{top:268px}
  .temp{position:absolute;left:0;width:232px;top:208px;text-align:center;font-weight:200;font-size:44px;letter-spacing:2px;display:flex;justify-content:center;align-items:center;gap:4px}
  .temp svg{width:14px;height:30px}
  .unit-toggle{position:absolute;left:183px;top:250px;width:12px;height:12px;background:#d9dde0}
  .unit-toggle::after{content:"°C";position:absolute;left:14px;top:-1px;font-size:9px;color:var(--sky-blue);font-weight:600}
  .stats{position:absolute;left:0;top:292px;width:232px;height:58px;background:var(--strip);display:flex}
  .stat{flex:1;display:flex;align-items:center;justify-content:center;gap:6px;font-size:16px;font-weight:400}
  .stat + .stat{border-left:1px solid rgba(255,255,255,.15)}
  .stat svg{flex:none}
  .ring{position:relative;width:46px;height:46px}
  .ring span{position:absolute;inset:0;display:flex;align-items:center;justify-content:center;font-size:14px;font-weight:600}
  .forecast{position:absolute;left:0;top:350px;width:232px;height:42px;background:var(--sky-blue);list-style:none;display:flex}
  .day{flex:1;text-align:center;font-size:8px;font-weight:600;padding-top:4px}
  .day .row{display:flex;justify-content:center;align-items:center;gap:2px;margin-top:2px;line-height:9px}
  .day svg{width:15px;height:12px}
  .day .range{text-align:left;font-size:7.5px}
</style>
</head>
<body>
<svg width="0" height="0" style="position:absolute" aria-hidden="true">
  <defs>
    <symbol id="icon-cloud-snow" viewBox="0 0 108 86">
      <path d="M30 62 H22 A18 18 0 0 1 26 26 A27 27 0 0 1 76 22 A20 20 0 0 1 88 62 H78" fill="none" stroke="#fff" stroke-width="8" stroke-linecap="round" stroke-linejoin="round"/>
      <g fill="#fff" transform="translate(54 66)">
        <circle r="5"/><circle cy="-9" r="5"/><circle cy="9" r="5"/>
        <circle cx="8" cy="-4.5" r="5"/><circle cx="-8" cy="-4.5" r="5"/>
        <circle cx="8" cy="4.5" r="5"/><circle cx="-8" cy="4.5" r="5"/>
      </g>
    </symbol>
    <symbol id="icon-cloud-rain" viewBox="0 0 108 86">
      <path d="M22 62 A18 18 0 0 1 26 26 A27 27 0 0 1 76 22 A20 20 0 0 1 88 62" fill="none" stroke="#fff" stroke-width="8" stroke-linecap="round"/>
      <g stroke="#fff" stroke-width="8" stroke-linecap="round">
        <line x1="40" y1="46" x2="40" y2="74"/><line x1="54" y1="46" x2="54" y2="78"/><line x1="68" y1="46" x2="68" y2="74"/>
      </g>
    </symbol>
    <symbol id="icon-sun-cloud" viewBox="0 0 40 32">
      <g stroke="#fff" stroke-width="2" stroke-linecap="round" fill="none">
        <circle cx="25" cy="12" r="6"/>
        <line x1="25" y1="1" x2="25" y2="3"/><line x1="34" y1="4" x2="32.5" y2="5.5"/><line x1="37" y1="12" x2="35" y2="12"/><line x1="16" y1="4" x2="17.5" y2="5.5"/>
        <path d="M10 29 H26 A6 6 0 0 0 26 17 A9 9 0 0 0 9 17 A6 6 0 0 0 10 29Z" fill="var(--sky-blue)"/>
      </g>
    </symbol>
    <symbol id="icon-thermo" viewBox="0 0 14 30">
      <rect x="4" y="1" width="6" height="20" rx="3" fill="none" stroke="#fff" stroke-width="2"/>
      <circle cx="7" cy="24" r="5" fill="#fff"/><rect x="6" y="9" width="2" height="14" fill="#fff"/>
    </symbol>
    <symbol id="icon-drop" viewBox="0 0 24 24">
      <circle cx="12" cy="12" r="10" fill="none" stroke="#fff" stroke-width="2.5"/>
      <path d="M12 6 C9 10 8.5 12 8.5 13.5 A3.5 3.5 0 0 0 15.5 13.5 C15.5 12 15 10 12 6Z" fill="#fff"/>
    </symbol>
    <symbol id="icon-wind" viewBox="0 0 30 20">
      <g fill="none" stroke="#fff" stroke-width="2" stroke-linecap="round">
        <path d="M2 7 H20 A4 4 0 1 0 16 3"/><path d="M2 12 H24 A3.5 3.5 0 1 1 21 16"/><path d="M6 16 H14"/>
      </g>
    </symbol>
  </defs>
</svg>

<main class="canvas">
  <!-- variant with curved callout arrows -->
  <section class="panel left">
    <h1 class="headline"><span class="app-name">THERMOMETER</span><span class="platform">for Orbphone</span></h1>

    <svg class="callouts" viewBox="0 0 568 560">
      <circle cx="452" cy="300" r="106" fill="var(--sky-blue)"/>
      <use href="#icon-sun-cloud" x="418" y="238" width="48" height="38"/>
      <use href="#icon-thermo" x="424" y="298" width="11" height="24"/>
      <text class="reading" x="441" y="320">25°</text>
      <use href="#icon-thermo" x="424" y="334" width="11" height="24"/>
      <text class="reading" x="441" y="356">19°</text>
      <use href="#icon-drop" x="412" y="378" width="26" height="26"/>
      <use href="#icon-wind" x="458" y="380" width="30" height="20"/>
      <text x="375" y="214">Weather Icon</text>
      <text x="285" y="292">High</text><text x="285" y="320">Temp</text>
      <text x="292" y="362">Low</text><text x="292" y="390">Temp</text>
      <text x="285" y="474">Wind Speed</text><text x="285" y="502">and direction</text>
      <text x="455" y="498">Humidity</text>
      <g fill="none" stroke="#fff" stroke-width="1.4" stroke-linecap="round">
        <path d="M416 278 C360 270 335 250 350 215"/><path d="M346 222 L350 213 L356 221"/>
        <path d="M420 318 C385 315 365 302 350 292"/><path d="M352 298 L348 291 L357 290"/>
        <path d="M420 350 C390 345 365 340 340 355"/><path d="M342 349 L338 357 L347 358"/>
        <path d="M414 398 C380 400 345 420 330 448"/><path d="M329 440 L329 450 L337 444"/>
        <path d="M480 402 C500 420 500 455 490 470"/><path d="M486 463 L489 472 L496 466"/>
      </g>
    </svg>

    <article class="screen snow" style="left:33px;top:117px">
      <div class="scene" role="img" aria-label="Photo of snow-covered mountain peaks under low cloud"></div>
      <span class="location">LONDON, UK</span>
      <svg class="condition-icon"><use href="#icon-cloud-snow"/></svg>
      <p class="condition">Snow</p>
      <div class="rule upper"></div>
      <p class="temp"><svg><use href="#icon-thermo"/></svg>-5°C</p>
      <div class="rule lower"></div>
      <span class="unit-toggle"></span>
      <div class="stats">
        <div class="stat"><svg width="20" height="14"><use href="#icon-wind" width="20" height="14"/></svg>
          <div class="ring"><svg width="46" height="46"><circle cx="23" cy="23" r="19" fill="none" stroke="var(--ring-track)" stroke-width="5"/><circle cx="23" cy="23" r="19" fill="none" stroke="var(--sky-blue)" stroke-width="5" stroke-dasharray="72 120" transform="rotate(90 23 23)"/></svg><span>30%</span></div></div>
        <div class="stat"><svg width="16" height="16"><use href="#icon-drop" width="16" height="16"/></svg>N 39 km/h</div>
      </div>
      <ul class="forecast">
        <li class="day">MON<div class="row"><svg><use href="#icon-sun-cloud"/></svg><div class="range">25°<br>19°</div></div></li>
        <li class="day">TUES<div class="row"><svg><use href="#icon-sun-cloud"/></svg><div class="range">19°<br>14°</div></div></li>
        <li class="day">WEDS<div class="row"><svg><use href="#icon-sun-cloud"/></svg><div class="range">12°<br>6°</div></div></li>
        <li class="day">THURS<div class="row"><svg><use href="#icon-sun-cloud"/></svg><div class="range">25°<br>19°</div></div></li>
      </ul>
    </article>

    <article class="screen rain" style="left:300px;top:568px">
      <div class="scene" role="img" aria-label="Photo of raindrops running down a window pane"></div>
      <span class="location">LONDON, UK</span>
      <svg class="condition-icon"><use href="#icon-cloud-rain"/></svg>
      <p class="condition">Rain</p>
      <div class="rule upper"></div>
      <p class="temp"><svg><use href="#icon-thermo"/></svg>9°C</p>
      <div class="rule lower"></div>
      <span class="unit-toggle"></span>
      <div class="stats">
        <div class="stat"><svg width="20" height="14"><use href="#icon-wind" width="20" height="14"/></svg>
          <div class="ring"><svg width="46" height="46"><circle cx="23" cy="23" r="19" fill="none" stroke="var(--ring-track)" stroke-width="5"/><circle cx="23" cy="23" r="19" fill="none" stroke="var(--sky-blue)" stroke-width="5" stroke-dasharray="72 120" transform="rotate(90 23 23)"/></svg><span>30%</span></div></div>
        <div class="stat"><svg width="16" height="16"><use href="#icon-drop" width="16" height="16"/></svg>N 39 km/h</div>
      </div>
      <ul class="forecast">
        <li class="day">MON<div class="row"><svg><use href="#icon-sun-cloud"/></svg><div class="range">25°<br>19°</div></div></li>
        <li class="day">TUES<div class="row"><svg><use href="#icon-sun-cloud"/></svg><div class="range">19°<br>14°</div></div></li>
        <li class="day">WEDS<div class="row"><svg><use href="#icon-sun-cloud"/></svg><div class="range">12°<br>6°</div></div></li>
        <li class="day">THURS<div class="row"><svg><use href="#icon-sun-cloud"/></svg><div class="range">25°<br>19°</div></div></li>
      </ul>
    </article>
  </section>

  <!-- variant with straight leader lines -->
  <section class="panel right">
    <h1 class="headline"><span class="app-name">THERMOMETER</span><span class="platform">for Orbphone</span></h1>

    <svg class="callouts" viewBox="0 0 568 560">
      <circle cx="431" cy="320" r="96" fill="var(--sky-blue)"/>
      <use href="#icon-sun-cloud" x="424" y="242" width="58" height="46"/>
      <use href="#icon-thermo" x="428" y="310" width="11" height="24"/>
      <text class="reading" x="447" y="332">25°</text>
      <use href="#icon-thermo" x="428" y="348" width="11" height="24"/>
      <text class="reading" x="447" y="370">19°</text>
      <use href="#icon-drop" x="419" y="385" width="24" height="24"/>
      <use href="#icon-wind" x="471" y="388" width="28" height="18"/>
      <text x="290" y="230">Weather</text><text x="290" y="259">Icon</text>
      <text x="286" y="305">High</text><text x="286" y="333">Temp</text>
      <text x="292" y="375">Low</text><text x="292" y="403">Temp</text>
      <text x="302" y="462">Wind Speed</text><text x="302" y="491">and direction</text>
      <text x="464" y="485">Humidity</text>
      <g stroke="#fff" stroke-width="1.2">
        <line x1="330" y1="259" x2="440" y2="259"/>
        <line x1="346" y1="325" x2="426" y2="325"/>
        <line x1="345" y1="364" x2="426" y2="364"/>
        <line x1="380" y1="443" x2="424" y2="408"/>
        <line x1="485" y1="412" x2="485" y2="462"/>
      </g>
    </svg>

    <article class="screen snow" style="left:36px;top:117px">
      <div class="scene" role="img" aria-label="Photo of snow-covered mountain peaks under low cloud"></div>
      <span class="location">LONDON, UK</span>
      <svg class="condition-icon"><use href="#icon-cloud-snow"/></svg>
      <p class="condition">Snow</p>
      <div class="rule upper"></div>
      <p class="temp"><svg><use href="#icon-thermo"/></svg>-5°C</p>
      <div class="rule lower"></div>
      <span class="unit-toggle"></span>
      <div class="stats">
        <div class="stat"><svg width="20" height="14"><use href="#icon-wind" width="20" height="14"/></svg>
          <div class="ring"><svg width="46" height="46"><circle cx="23" cy="23" r="19" fill="none" stroke="var(--ring-track)" stroke-width="5"/><circle cx="23" cy="23" r="19" fill="none" stroke="var(--sky-blue)" stroke-width="5" stroke-dasharray="72 120" transform="rotate(90 23 23)"/></svg><span>30%</span></div></div>
        <div class="stat"><svg width="16" height="16"><use href="#icon-drop" width="16" height="16"/></svg>N 39 km/h</div>
      </div>
      <ul class="forecast">
        <li class="day">MON<div class="row"><svg><use href="#icon-sun-cloud"/></svg><div class="range">25°<br>19°</div></div></li>
        <li class="day">TUES<div class="row"><svg><use href="#icon-sun-cloud"/></svg><div class="range">19°<br>14°</div></div></li>
        <li class="day">WEDS<div class="row"><svg><use href="#icon-sun-cloud"/></svg><div class="range">12°<br>6°</div></div></li>
        <li class="day">THURS<div class="row"><svg><use href="#icon-sun-cloud"/></svg><div class="range">25°<br>19°</div></div></li>
      </ul>
    </article>

    <article class="screen rain" style="left:300px;top:568px">
      <div class="scene" role="img" aria-label="Photo of raindrops running down a window pane"></div>
      <span class="location">LONDON, UK</span>
      <svg class="condition-icon"><use href="#icon-cloud-rain"/></svg>
      <p class="condition">Rain</p>
      <div class="rule upper"></div>
      <p class="temp"><svg><use href="#icon-thermo"/></svg>9°C</p>
      <div class="rule lower"></div>
      <span class="unit-toggle"></span>
      <div class="stats">
        <div class="stat"><svg width="20" height="14"><use href="#icon-wind" width="20" height="14"/></svg>
          <div class="ring"><svg width="46" height="46"><circle cx="23" cy="23" r="19" fill="none" stroke="var(--ring-track)" stroke-width="5"/><circle cx="23" cy="23" r="19" fill="none" stroke="var(--sky-blue)" stroke-width="5" stroke-dasharray="72 120" transform="rotate(90 23 23)"/></svg><span>30%</span></div></div>
        <div class="stat"><svg width="16" height="16"><use href="#icon-drop" width="16" height="16"/></svg>N 39 km/h</div>
      </div>
      <ul class="forecast">
        <li class="day">MON<div class="row"><svg><use href="#icon-sun-cloud"/></svg><div class="range">25°<br>19°</div></div></li>
        <li class="day">TUES<div class="row"><svg><use href="#icon-sun-cloud"/></svg><div class="range">19°<br>14°</div></div></li>
        <li class="day">WEDS<div class="row"><svg><use href="#icon-sun-cloud"/></svg><div class="range">12°<br>6°</div></div></li>
        <li class="day">THURS<div class="row"><svg><use href="#icon-sun-cloud"/></svg><div class="range">25°<br>19°</div></div></li>
      </ul>
    </article>
  </section>
</main>
</body>
</html>
```